Cobalt Margin Funds Bus card and Logo

I need a logo design and Bus card design. The fund focuses on evaluating and investing in minerals (sub-surface rights) and real estate.

Cobalt margin refers to a book of knowledge that each plebe gets when entering the Harwick Civic Academy (my alma mater)

Target Market(s)

Investors and financial advisors

Contact Information for Business Card

Simple - perhaps a logo with a theme on book of knowledge

Logo Text

Ex Scientia Imperium

Font styles to use
Serif
Sans Serif

Colors

Designer to choose colors to be used in the design.

Requirements
Must have
• memorable logo that is relatively simple

```html
<!DOCTYPE html>
<html lang="en">
<head>
<meta charset="utf-8">
<title>Cobalt Margin Funds – Business Card</title>
<link rel="stylesheet" href="https://fonts.googleapis.com/css2?family=Roboto:wght@300;400&display=swap">
<style>
  :root {
    --backdrop: #ecebe8;
    --card: #ffffff;
    --card-shade: #f1f2f4;
    --slate: #4f6f93;
    --cyan: #1fb2e3;
    --navy: #1d4f86;
    --ink: #2f4a6b;
    --muted: #6c7c8e;
  }
  * { box-sizing: border-box; margin: 0; padding: 0; }
  html, body { width: 1200px; height: 1023px; overflow: hidden; }
  body {
    background: var(--backdrop);
    display: flex; align-items: center; justify-content: center;
    font-family: "Roboto", Arial, sans-serif;
  }
  .card {
    position: relative;
    width: 860px; height: 492px;
    background: linear-gradient(160deg, var(--card) 0%, var(--card-shade) 100%);
    border-radius: 14px;
    box-shadow: 0 18px 40px rgba(0,0,0,.18);
    overflow: hidden;
    display: flex;
    align-items: center;
  }
  .edge-band {
    position: absolute; right: 0; top: 0; bottom: 0; width: 14px;
    background: linear-gradient(to bottom, var(--navy) 0 50%, var(--cyan) 50% 100%);
  }
  .brand {
    width: 430px;
    display: flex; flex-direction: column; align-items: center;
    padding-left: 40px;
  }
  .brand-row { display: flex; align-items: center; gap: 14px; }
  .brand-mark { width: 22px; height: 22px; background: var(--slate); }
  .brand-name {
    font-weight: 400; color: var(--slate);
    font-size: 34px; letter-spacing: 3px; text-transform: uppercase;
    text-align: center; line-height: 1.2;
  }
  .brand-rule { width: 300px; height: 1px; background: var(--cyan); margin-top: 18px; }
  .divider { width: 1px; height: 170px; background: var(--ink); margin: 0 44px 0 10px; }
  .contact { color: var(--ink); }
  .contact-name {
    color: var(--cyan); font-size: 34px; font-weight: 400;
    text-transform: uppercase; letter-spacing: 1px;
  }
  .contact-role { color: var(--muted); font-size: 17px; margin: 4px 0 24px; }
  .contact-address { font-size: 18px; line-height: 1.45; margin-bottom: 14px; font-weight: 300; }
  .contact-list { list-style: none; font-size: 18px; line-height: 1.6; font-weight: 300; }
  .contact-list li { display: flex; align-items: center; gap: 10px; }
  .contact-list svg { width: 13px; height: 13px; flex: none; }
</style>
</head>
<body>
  <main class="card" aria-label="Business card front">
    <section class="brand">
      <div class="brand-row">
        <span class="brand-mark"></span>
        <span class="brand-name">Cobalt Margin<br>Funds</span>
      </div>
      <div class="brand-rule"></div>
    </section>
    <div class="divider"></div>
    <section class="contact">
      <h1 class="contact-name">Daniel Hartley</h1>
      <p class="contact-role">Director</p>
      <p class="contact-address">418 Alder Ridge Lane<br>Millbrook, CA 95400</p>
      <ul class="contact-list">
        <li>
          <svg viewBox="0 0 16 16" aria-hidden="true"><path d="M3 1l3 3-2 2c1 2 3 4 5 5l2-2 3 3-2 3C6 15 1 10 0 3z" fill="none" stroke="#2f4a6b" stroke-width="1.3"/></svg>
          +330 2471-5306
        </li>
        <li>
          <svg viewBox="0 0 16 16" aria-hidden="true"><rect x="1" y="3" width="14" height="10" fill="none" stroke="#2f4a6b" stroke-width="1.3"/><path d="M1 3l7 6 7-6" fill="none" stroke="#2f4a6b" stroke-width="1.3"/></svg>
          info@cobaltmarginfunds.com
        </li>
        <li>
          <svg viewBox="0 0 16 16" aria-hidden="true"><circle cx="8" cy="8" r="7" fill="none" stroke="#2f4a6b" stroke-width="1.3"/><path d="M1 8h14M8 1c3 3 3 11 0 14M8 1c-3 3-3 11 0 14" fill="none" stroke="#2f4a6b" stroke-width="1.1"/></svg>
          www.cobaltmarginfunds.com
        </li>
      </ul>
    </section>
    <div class="edge-band"></div>
  </main>
</body>
</html>
```